Salad Dressing Bottle Design

Looking for a design for front of salad dressing bottle. Must have sesame theme to be obvious

Australian theme.

Marlow Creek Sesame Dressing

Gluten Free
Vegan

100% Australian Grown Sesame Seeds
150gm

Colors
00AB8E
00BBA5
67D7C9
C6EFE9
E9F9F6
FFC000
F8CF3A
FAE287
FDF2CF
FEFAEE

```html
<!DOCTYPE html>
<html lang="en">
<head>
<meta charset="utf-8">
<title>Marlow Creek Sesame Dressing – Label</title>
<link rel="stylesheet" href="https://fonts.googleapis.com/css2?family=Bebas+Neue&family=Roboto:ital,wght@0,300;0,400;0,500;1,700&display=swap">
<style>
  :root {
    --teal: #00AB8E;
    --teal-mid: #00BBA5;
    --teal-soft: #67D7C9;
    --teal-pale: #C6EFE9;
    --teal-mist: #E9F9F6;
    --gold: #FFC000;
    --gold-warm: #F8CF3A;
    --gold-soft: #FAE287;
    --gold-pale: #FDF2CF;
    --cream: #FEFAEE;
    --ink-teal: #005C4D;
    --sesame-light: #E4B978;
    --sesame-dark: #A86F35;
    --page-bg: #f3f3f3;
  }
  html, body {
    margin: 0;
    padding: 0;
    overflow: hidden;
  }
  .canvas {
    position: relative;
    width: 1200px;
    height: 1200px;
    background: var(--page-bg);
    overflow: hidden;
  }
  .body-label {
    position: absolute;
    left: 250px;
    top: 100px;
    width: 493px;
    height: 1001px;
  }
  .neck-label {
    position: absolute;
    left: 800px;
    top: 100px;
    width: 315px;
    height: 140px;
  }
  .fill-teal { fill: var(--teal); }
  .fill-gold { fill: var(--gold); }
  .wave-edge { stroke: var(--cream); stroke-width: 14; paint-order: stroke; }
  .star-light { fill: var(--cream); }
  .star-teal { fill: var(--teal); }
  .product-name {
    font-family: "Bebas Neue", "Oswald", sans-serif;
    font-size: 47px;
    fill: var(--cream);
  }
  .claim {
    font-family: "Roboto", Arial, sans-serif;
    font-weight: 500;
    font-size: 20px;
    fill: var(--ink-teal);
  }
  .percent {
    font-family: "Roboto", Arial, sans-serif;
    font-weight: 300;
    font-size: 28px;
    fill: var(--ink-teal);
  }
  .origin {
    font-family: "Roboto", Arial, sans-serif;
    font-style: italic;
    font-weight: 700;
    font-size: 15px;
    fill: var(--ink-teal);
  }
  .net-weight {
    font-family: "Bebas Neue", "Oswald", sans-serif;
    font-size: 44px;
    fill: var(--cream);
  }
</style>
</head>
<body>
<div class="canvas">

  <svg class="body-label" viewBox="0 0 352 715" xmlns="http://www.w3.org/2000/svg">
    <defs>
      <symbol id="star" viewBox="-1 -1 2 2">
        <polygon points="0,-1 0.2245,-0.309 0.951,-0.309 0.3633,0.118 0.5878,0.809 0,0.382 -0.5878,0.809 -0.3633,0.118 -0.951,-0.309 -0.2245,-0.309"/>
      </symbol>
      <radialGradient id="sesame-tone" cx="50%" cy="40%" r="60%">
        <stop offset="0%" stop-color="#E4B978"/>
        <stop offset="100%" stop-color="#A86F35"/>
      </radialGradient>
      <clipPath id="label-shape">
        <path d="M0,50 C40,5 110,-5 180,10 C250,25 300,15 352,3 L352,715 L0,715 Z"/>
      </clipPath>
    </defs>

    <g clip-path="url(#label-shape)">
      <rect class="fill-teal" x="0" y="0" width="352" height="715"/>
      <path class="fill-gold wave-edge" d="M352,160 C250,170 175,215 150,320 C130,400 110,470 55,515 L0,560 L0,715 L352,715 Z"/>
      <path class="fill-teal wave-edge" d="M0,700 C100,715 200,690 270,650 C300,632 330,625 352,625 L352,715 L0,715 Z"/>
    </g>

    <text class="product-name" x="174" y="63" text-anchor="middle">MARLOW CREEK</text>
    <text class="product-name" x="174" y="119" text-anchor="middle">SESAME DRESSING</text>

    <g class="stars-light star-light">
      <use href="#star" x="187" y="142" width="24" height="24"/>
      <use href="#star" x="110" y="181" width="28" height="28"/>
      <use href="#star" x="53" y="246" width="34" height="34"/>
      <use href="#star" x="28" y="340" width="50" height="50"/>
      <use href="#star" x="40" y="448" width="24" height="24"/>
    </g>
    <g class="stars-teal star-teal">
      <use href="#star" x="216" y="214" width="36" height="36"/>
      <use href="#star" x="161" y="273" width="24" height="24"/>
      <use href="#star" x="144" y="351" width="12" height="12"/>
    </g>

    <text class="claim" x="325" y="336" text-anchor="end">Gluten Free</text>
    <text class="claim" x="325" y="362" text-anchor="end">Vegan</text>
    <text class="percent" x="321" y="418" text-anchor="end">100%</text>
    <text class="origin" x="325" y="439" text-anchor="end">Australian Grown</text>
    <text class="origin" x="325" y="459" text-anchor="end">Sesame Seeds</text>

    <g role="img" aria-label="Pile of roasted golden sesame seeds">
      <ellipse cx="150" cy="565" rx="140" ry="55" fill="url(#sesame-tone)"/>
    </g>

    <text class="net-weight" x="339" y="696" text-anchor="end">150 GM</text>
  </svg>

  <svg class="neck-label" viewBox="0 0 225 100" xmlns="http://www.w3.org/2000/svg">
    <defs>
      <symbol id="neck-star" viewBox="-1 -1 2 2">
        <polygon points="0,-1 0.2245,-0.309 0.951,-0.309 0.3633,0.118 0.5878,0.809 0,0.382 -0.5878,0.809 -0.3633,0.118 -0.951,-0.309 -0.2245,-0.309" fill="#FEFAEE"/>
      </symbol>
    </defs>
    <rect class="fill-teal" x="0" y="0" width="225" height="50"/>
    <rect class="fill-gold" x="0" y="50" width="225" height="50"/>
    <use href="#neck-star" x="44" y="32" width="34" height="34"/>
    <use href="#neck-star" x="95" y="32" width="34" height="34"/>
    <use href="#neck-star" x="145" y="32" width="34" height="34"/>
  </svg>

</div>
</body>
</html>
```